Business card design needed

New company based in Brisbane, Australia. Brindle Systems. The business is focused on the delivery of network architecture design and deployment. We will provide both services and the sale of the necessary equipment to deliver the service. Cloud computing is an important element of our focus as this is an emerging market for enterprises in Queensland. Our target marketplace is medium to large corporations with complex infrastructure requirements. IT Management and above will be the typical entry point for us into these accounts. We would like to see the use of various shade of green, design should be clutter free and impress stability, trust and growth.
Updates
Hey Everyone
Just we let you all know we have changed this project to 'committed' payment status.
Looking forward to seeing the designs! Thanks for your efforts.
Best Regards
Marcus
Industry/Entity Type
Architecture
Contact Information for Business Card
Brindle Systems, Marcus Doyle, Sales Director, Level 14 Harlow Tower, 58 Penfold Street, Brisbane QLD 4000, Ph +61 7 3904 2267, M +61 4 4926 1573, E marcus.doyle@brindlesystems-example.com.au
Look and feel
Each slider illustrates characteristics of the customer's brand and the style your logo design should communicate.

```html
<!DOCTYPE html>
<html lang="en">
<head>
<meta charset="utf-8">
<title>Brindle Systems — Business Card</title>
<link rel="stylesheet" href="https://fonts.googleapis.com/css2?family=Barlow:wght@400;500;700&display=swap">
<style>
  :root {
    --page-bg: #e9ecea;
    --card-front: #f4f6f5;
    --brand-green: #2e8b57;
    --brand-green-deep: #1d6a42;
    --brand-green-light: #5cbf7e;
    --brand-green-pale: rgba(140, 215, 160, 0.55);
    --text-grey: #555a5e;
    --rule-grey: #c4cac6;
    --white: #ffffff;
  }
  * { box-sizing: border-box; margin: 0; padding: 0; }
  html, body {
    width: 1200px; height: 880px; overflow: hidden;
    background: var(--page-bg);
    font-family: "Barlow", Arial, sans-serif;
  }
  .sheet {
    width: 1200px; height: 880px;
    display: flex; align-items: center; justify-content: center; gap: 40px;
  }
  .card {
    width: 560px; height: 320px; position: relative; overflow: hidden;
    box-shadow: 0 6px 18px rgba(0, 0, 0, 0.12);
  }

  /* Front */
  .card-front { background: var(--card-front); }
  .front-brand {
    position: absolute; left: 26px; top: 148px; width: 180px;
    display: flex; flex-direction: column; align-items: center; gap: 10px;
  }
  .front-brand .brand-dot {
    width: 46px; height: 46px; border-radius: 50%; background: var(--brand-green);
  }
  .front-brand .brand-name {
    font-weight: 700; font-size: 21px; color: var(--text-grey);
    white-space: nowrap; line-height: 1;
  }
  .contact-block {
    position: absolute; right: 26px; top: 48px; width: 330px; text-align: right;
    color: var(--text-grey);
  }
  .person-name { font-weight: 700; font-size: 25px; line-height: 1.15; color: var(--brand-green); }
  .person-title { font-size: 15px; margin-top: 2px; }
  .rule { height: 1px; background: var(--rule-grey); margin: 10px 0; }
  .contact-row {
    display: flex; justify-content: flex-end; align-items: center; gap: 9px;
    font-size: 14px; line-height: 25px; white-space: nowrap;
  }
  .contact-row svg { width: 13px; height: 13px; flex: none; }
  .icon-fill { fill: var(--brand-green); }
  .icon-line { fill: none; stroke: var(--brand-green); stroke-width: 1.8; stroke-linejoin: round; }
  .address-row { align-items: flex-end; line-height: 22px; }
  .address-row svg { width: 14px; height: 18px; margin-bottom: 4px; }

  /* Back */
  .card-back { background: var(--brand-green-deep); }
  .back-field {
    position: absolute; inset: 0;
    background:
      radial-gradient(ellipse at 28% 30%, var(--brand-green-pale), transparent 55%),
      radial-gradient(ellipse at 20% 88%, rgba(20, 90, 55, 0.7), transparent 50%),
      linear-gradient(135deg, var(--brand-green-deep) 0%, var(--brand-green) 48%, var(--brand-green-light) 100%);
  }
  .website {
    position: absolute; left: 30px; top: 36px;
    font-size: 15px; color: var(--white); letter-spacing: 0.3px;
  }
  .back-brand {
    position: absolute; right: 40px; bottom: 58px;
    display: flex; flex-direction: column; align-items: center; gap: 12px;
  }
  .back-brand .brand-dot {
    width: 58px; height: 58px; border-radius: 50%; background: var(--white);
  }
  .back-brand .brand-name {
    font-weight: 700; font-size: 28px; color: var(--white);
    white-space: nowrap; line-height: 1;
  }
</style>
</head>
<body>
<main class="sheet">

  <section class="card card-front" aria-label="Business card front">
    <div class="front-brand">
      <span class="brand-dot"></span>
      <span class="brand-name">Brindle Systems</span>
    </div>

    <div class="contact-block">
      <h1 class="person-name">Marcus Doyle</h1>
      <p class="person-title">Sales Director</p>
      <div class="rule"></div>
      <p class="contact-row">+61 7 3904 2267
        <svg viewBox="0 0 16 16" aria-hidden="true"><rect class="icon-line" x="2" y="2" width="12" height="12" rx="2"/><rect class="icon-fill" x="5" y="5" width="6" height="2"/></svg>
      </p>
      <p class="contact-row">+61 4 4926 1573
        <svg viewBox="0 0 16 16" aria-hidden="true"><rect class="icon-line" x="4.5" y="1.5" width="7" height="13" rx="1.5"/></svg>
      </p>
      <p class="contact-row">marcus.doyle@brindlesystems-example.com.au
        <svg viewBox="0 0 16 16" aria-hidden="true"><path class="icon-line" d="M1.5 3.5h13v9h-13z M1.5 3.5l6.5 5 6.5-5"/></svg>
      </p>
      <div class="rule"></div>
      <p class="contact-row address-row"><span>Level 14 Harlow Tower, 58 Penfold Street<br>Brisbane QLD 4000</span>
        <svg viewBox="0 0 14 18" aria-hidden="true"><path class="icon-fill" d="M7 0a7 7 0 0 0-7 7c0 5 7 11 7 11s7-6 7-11a7 7 0 0 0-7-7zm0 10a3 3 0 1 1 0-6 3 3 0 0 1 0 6z"/></svg>
      </p>
    </div>
  </section>

  <section class="card card-back" aria-label="Business card back">
    <div class="back-field" role="img" aria-label="Flowing green wave decoration"></div>
    <p class="website">www.brindlesystems-example.com.au</p>
    <div class="back-brand">
      <span class="brand-dot"></span>
      <span class="brand-name">Brindle Systems</span>
    </div>
  </section>

</main>
</body>
</html>
```